Webdesign für Personalvermittlung
Zielgruppe
Personalvermittlung
Aufgabenstellung
es soll einladend - nicht zu überladen und natürlich cool und modern sein

```html
<!DOCTYPE html>
<html lang="de">
<head>
<meta charset="utf-8">
<title>PFLEGEWEG JOB – Karriere in der Pflege</title>
<link href="https://fonts.googleapis.com/css2?family=Poppins:ital,wght@0,400;0,500;0,600;0,700;0,800;1,400;1,500;1,600&display=swap" rel="stylesheet">
<style>
:root{
  --green:#5cb82e;
  --green-dark:#4aa321;
  --blue:#2b9be0;
  --blue-light:#e3f3fb;
  --text:#333;
  --muted:#777;
  --footer:#25232f;
}
*{box-sizing:border-box;margin:0;padding:0}
html,body{width:1200px;height:5168px;overflow:hidden}
body{font-family:'Poppins',sans-serif;color:var(--text);background:#fff;position:relative}
.abs{position:absolute}
.btn{display:inline-block;background:var(--green);color:#fff;font-weight:600;text-transform:uppercase;font-size:15px;text-align:center;letter-spacing:.3px}
.green{color:var(--green)}
.ital{font-style:italic}
/* header */
.header{position:absolute;top:0;left:0;width:1200px;height:108px}
.brand{position:absolute;left:74px;top:26px;display:flex;align-items:center;gap:10px;font-weight:700;font-size:17px;color:#2a3a66}
.brand-dot{width:40px;height:40px;border-radius:50%;background:var(--blue)}
.head-info{position:absolute;right:80px;top:30px;display:flex;align-items:center;gap:24px;font-size:12px}
.head-info .phone{color:var(--blue);display:flex;gap:6px;align-items:center}
.head-info .btn{padding:8px 18px;border-radius:4px;font-size:15px}
.nav{position:absolute;top:108px;left:0;width:1200px;height:64px;background:var(--blue);display:flex;align-items:center;color:#fff;font-weight:500;font-size:19px}
.nav a{position:absolute;color:#fff;text-decoration:none}
.nav .active{left:80px;top:0;width:157px;height:64px;background:var(--green);display:flex;align-items:center;justify-content:center}
/* hero */
.hero{position:absolute;top:172px;left:0;width:1200px;height:728px;background:linear-gradient(100deg,#e4edf3 0%,#c9dbe7 45%,#9fbcd6 70%,#dfe7ec 100%)}
.hero h1{position:absolute;left:100px;top:155px;font-size:41px;font-weight:700;line-height:50px;color:#1e1e1e}
.hero h1 span{display:block;color:var(--green);font-size:52px;font-weight:800;line-height:64px}
.hero p{position:absolute;left:102px;top:345px;font-size:27px;font-weight:600;line-height:42px;color:#222}
.hero .btn{position:absolute;left:101px;top:506px;padding:18px 16px;border-radius:4px;font-size:15px;box-shadow:0 3px 6px rgba(0,0,0,.2)}
.dots{position:absolute;left:760px;top:680px;display:flex;gap:14px}
.dots i{width:86px;height:10px;border-radius:5px;background:rgba(255,255,255,.7)}
.dots i.on{background:var(--green)}
/* stats */
.stats{position:absolute;top:900px;left:0;width:1200px;height:205px;display:flex;justify-content:center;align-items:center;gap:22px}
.stat{display:flex;align-items:center;gap:12px}
.stat b{font-size:74px;font-weight:700;color:var(--blue);line-height:1}
.stat em{font-size:19px;color:var(--green);line-height:28px}
.sep{width:3px;height:76px;background:#ddd}
/* offer */
.offer{position:absolute;top:1105px;left:0;width:1200px;height:615px;background:linear-gradient(90deg,#e7f5fb,#d9eef8)}
.offer h2{position:absolute;left:92px;top:22px;font-size:34px;font-weight:600;color:var(--green);line-height:42px}
.offer .rule{position:absolute;left:92px;top:192px;width:385px;height:1px;background:#bbb}
.checks{position:absolute;left:96px;top:210px;list-style:none}
.checks li{display:flex;align-items:center;gap:24px;height:54px;font-style:italic;font-size:18px}
.video{position:absolute;left:590px;top:35px;width:525px;height:305px;border-radius:16px;background:var(--blue);padding:14px}
.video div{width:100%;height:100%;border-radius:10px;background:linear-gradient(90deg,#f4f8fb 0%,#cfe0ec 55%,#8eaac4 100%);display:flex;align-items:center;justify-content:center}
.offer .copy{position:absolute;left:615px;top:415px;font-size:19px;font-style:italic;font-weight:600;line-height:28px;width:520px}
.offer .btn{position:absolute;left:612px;top:545px;width:242px;height:50px;line-height:50px}
/* expect */
.expect{position:absolute;top:1720px;left:0;width:1200px;height:980px}
.sec-title{position:absolute;left:0;width:1200px;text-align:center;color:var(--green);font-weight:600}
.sec-rule{position:absolute;left:297px;width:624px;height:2px;background:var(--blue)}
.sec-sub{position:absolute;left:0;width:1200px;text-align:center;font-style:italic;font-size:19px;color:#555}
.germany{position:absolute;left:380px;top:230px;width:420px;height:720px;background:radial-gradient(ellipse at center,#d2d2d2 0%,#e2e2e2 60%,rgba(255,255,255,0) 75%)}
.feat{position:absolute;width:260px}
.feat h3{font-size:23px;font-weight:600;color:var(--green);line-height:34px;margin-left:76px}
.feat p{font-size:14px;color:#666;line-height:26px;margin:14px 0 0 76px;width:240px}
.feat svg{position:absolute;left:0;top:2px}
/* about */
.about{position:absolute;top:2700px;left:0;width:1200px;height:415px;background:var(--blue-light)}
.about p{position:absolute;left:150px;top:180px;width:900px;text-align:center;font-size:14px;font-style:italic;line-height:26px}
.about .btn{position:absolute;left:500px;top:318px;width:204px;height:52px;line-height:52px}
/* reviews */
.reviews{position:absolute;top:3115px;left:0;width:1200px;height:565px;overflow:hidden}
.card{position:absolute;background:#fff;border-radius:10px;box-shadow:0 4px 14px rgba(0,0,0,.15);padding:20px;font-size:13px;text-align:center;line-height:21px}
.quote{font-size:58px;font-weight:800;color:var(--green);line-height:40px}
.who{display:flex;align-items:center;gap:16px;margin-top:18px;text-align:left}
.avatar{width:92px;height:92px;border-radius:50%;background:linear-gradient(135deg,#c7d3dc,#7f96a8);flex:none}
.who b{font-size:18px;font-weight:700;display:block}
.who span{font-size:17px}
.arrow{position:absolute;width:44px;height:44px;border-radius:50%;background:#fff;box-shadow:0 2px 8px rgba(0,0,0,.2);display:flex;align-items:center;justify-content:center}
/* contact */
.contact{position:absolute;top:3680px;left:0;width:1200px;height:750px}
.contact h2{position:absolute;left:108px;top:90px;font-size:32px;font-weight:600;color:var(--green);line-height:40px}
.field{position:absolute;font-size:13px}
.field label{display:block;margin-bottom:10px}
.field .box{border:1px solid #ccc;height:44px;padding:12px;font-size:12px;color:#aaa;font-style:italic}
.contact .send{position:absolute;left:108px;top:614px;width:554px;height:50px;line-height:50px}
.panel{position:absolute;left:700px;top:40px;width:500px;height:690px;background:linear-gradient(135deg,#def1fa,#eef8fd);overflow:hidden}
.panel h2{position:static;font-size:34px;color:var(--green);font-weight:600;margin:30px 0 0 18px}
.panel .role{font-size:26px;font-style:italic;margin:4px 0 0 18px}
.portrait{width:130px;height:135px;margin:14px 0 0 20px;border-radius:50%;background:linear-gradient(135deg,#e6e6e6,#7d8791)}
.panel .name{font-size:26px;font-weight:700;font-style:italic;margin:24px 0 0 24px}
.pline{display:flex;align-items:center;gap:16px;margin:14px 0 0 24px;font-size:16px;font-style:italic;font-weight:700}
.panel .addr{font-size:26px;font-style:italic;margin:20px 0 0 14px}
.corner{position:absolute;right:-90px;bottom:-90px;width:180px;height:180px;border-radius:50%;background:var(--green)}
/* map */
.map{position:absolute;top:4430px;left:0;width:1200px;height:460px;background:linear-gradient(135deg,#eef1ef,#dfe6e2 50%,#e9ecf0)}
/* footer */
.footer{position:absolute;top:4890px;left:0;width:1186px;height:240px;background:var(--footer);color:#fff}
.footer .brand{left:108px;top:60px;flex-direction:column;color:#fff;font-size:18px}
.socials{position:absolute;left:116px;top:176px;display:flex;gap:12px}
.socials i{width:22px;height:22px;background:var(--blue);display:block}
.footer h4{position:absolute;font-weight:400;font-style:italic;font-size:18px}
.footer ul{position:absolute;left:430px;top:98px;font-size:11px;font-style:italic;line-height:17px}
.newsletter{position:absolute;left:786px;top:96px;width:330px;height:46px;background:#fff;display:flex;align-items:center;gap:14px;padding:0 14px;font-size:12px;color:#aaa;font-style:italic}
.footer .note{position:absolute;left:786px;top:160px;width:330px;font-size:12px;font-style:italic;line-height:18px}
.copy-strip{position:absolute;top:5130px;left:0;width:1200px;text-align:center;font-size:13px;color:#2a3a88;line-height:38px}
</style>
</head>
<body>

<header class="header">
  <div class="brand"><span class="brand-dot"></span>PFLEGEWEG JOB</div>
  <div class="head-info">
    <span>Any Qirgendeine Frage</span>
    <span class="phone"><svg width="14" height="14" viewBox="0 0 24 24"><path fill="#2b9be0" d="M6.6 10.8a15 15 0 0 0 6.6 6.6l2.2-2.2c.3-.3.7-.4 1-.2 1.1.4 2.3.6 3.6.6.6 0 1 .4 1 1V20c0 .6-.4 1-1 1A17 17 0 0 1 3 4c0-.6.4-1 1-1h3.5c.6 0 1 .4 1 1 0 1.3.2 2.5.6 3.6.1.3 0 .7-.2 1z"/></svg>07000 123 456 7</span>
    <span class="btn">✎ Anwenden</span>
  </div>
</header>

<nav class="nav">
  <a class="active">Home</a>
  <a style="left:295px;top:19px">Wir Bieten Dir</a>
  <a style="left:540px;top:19px">Uber Uns</a>
  <a style="left:763px;top:19px">Kontakt</a>
</nav>

<section class="hero" role="img" aria-label="Foto: Pflegekräfte in Klinikkleidung mit verschränkten Armen">
  <h1>DEIN NÄCHSTER<br>KARRIERESCHRITT IM<span>PFLEGEBERUF!</span></h1>
  <p>Wir bieten Ihnen den perfekten<br>Job als Führungskraft!</p>
  <span class="btn">Ich will ein Angebot!</span>
  <svg class="abs" style="left:55px;top:290px" width="24" height="40"><path d="M20 4 6 20l14 16" stroke="#fff" stroke-width="3" fill="none"/></svg>
  <svg class="abs" style="left:1125px;top:290px" width="24" height="40"><path d="M4 4l14 16L4 36" stroke="#fff" stroke-width="3" fill="none"/></svg>
  <div class="dots"><i></i><i class="on"></i><i></i><i></i></div>
</section>

<section class="stats">
  <div class="stat"><b>15</b><em>Jahren<br>Erfahrung</em></div>
  <div class="sep"></div>
  <div class="stat"><b>100+</b><em>Mitglied</em></div>
  <div class="sep"></div>
  <div class="stat"><b>10+</b><em>Arbeitsplatz</em></div>
</section>

<section class="offer">
  <h2>Wir bieten Ihnen<br>den perfekten<br>Job als Führungskraft!</h2>
  <div class="rule"></div>
  <ul class="checks">
    <li><svg width="22" height="18"><path d="M2 9l6 6L20 3" stroke="#5cb82e" stroke-width="4" fill="none"/></svg>Wohnbereichsleiter/in</li>
    <li><svg width="22" height="18"><path d="M2 9l6 6L20 3" stroke="#5cb82e" stroke-width="4" fill="none"/></svg>Pflegedienstleiter/in</li>
    <li><svg width="22" height="18"><path d="M2 9l6 6L20 3" stroke="#5cb82e" stroke-width="4" fill="none"/></svg>Stationsleiter/in</li>
    <li><svg width="22" height="18"><path d="M2 9l6 6L20 3" stroke="#5cb82e" stroke-width="4" fill="none"/></svg>OP-Manager/in</li>
    <li><svg width="22" height="18"><path d="M2 9l6 6L20 3" stroke="#5cb82e" stroke-width="4" fill="none"/></svg>Heimleiter/in</li>
    <li><svg width="22" height="18"><path d="M2 9l6 6L20 3" stroke="#5cb82e" stroke-width="4" fill="none"/></svg>Klinikdirektor/in</li>
  </ul>
  <div class="video"><div role="img" aria-label="Video-Vorschau: Willkommensbild mit Pflegeteam"><svg width="56" height="56"><circle cx="28" cy="28" r="25" fill="none" stroke="#222" stroke-width="4"/><path d="M22 16l16 12-16 12z" fill="#222"/></svg></div></div>
  <p class="copy">und willst Dich verändern? Oder möchtest eine Weiterbildung in die Management-Ebene?<br><br>Dann nimm Kontakt zu uns auf...</p>
  <span class="btn">Wir bieten dir</span>
</section>

<section class="expect">
  <h2 class="sec-title" style="top:50px;font-size:33px;line-height:42px">Was darfst Du von<br>PFLEGEWEG-JOB.de erwarten?</h2>
  <div class="sec-rule" style="top:144px"></div>
  <p class="sec-sub" style="top:160px">Ihr Erfolg, unser Engagement</p>
  <div class="germany" role="img" aria-label="Landkarte von Deutschland als Hintergrund"></div>

  <div class="feat" style="left:104px;top:230px">
    <svg width="48" height="44"><rect x="2" y="10" width="44" height="32" rx="4" fill="#5cb82e"/><rect x="16" y="3" width="16" height="10" rx="2" fill="none" stroke="#5cb82e" stroke-width="4"/></svg>
    <h3>Zugriff auf mehr Stellen</h3>
    <p>In Zusammenarbeit mit Einrichtungen und Kliniken erhalten unsere Kandidaten einen zugesicherten Bonus in Höhe von 750 EUR für das Vertrauen bei Ihrem Jobwechsel in pflegeweg-job.de</p>
  </div>
  <div class="feat" style="left:446px;top:240px">
    <svg width="54" height="24"><rect width="54" height="20" rx="4" fill="#5cb82e"/></svg>
    <h3 style="margin-left:84px">100% kostenfrei</h3>
    <p style="margin-left:84px;width:250px">Unsere Dienstleistung ist für Dich als Bewerber 100% kostenfrei! Es gibt auch garantiert keine versteckten Kosten!</p>
  </div>
  <div class="feat" style="left:790px;top:236px">
    <svg width="48" height="24"><path d="M12 4a8 8 0 1 0 0 16c8 0 16-16 24-16a8 8 0 1 1 0 16C28 20 20 4 12 4z" fill="none" stroke="#5cb82e" stroke-width="5"/></svg>
    <h3>Dauerhafte Betreuung</h3>
    <p style="width:220px">Dein neuer Arbeitgeber hält nicht was er verspricht? Keine Sorge, wir werden für Dich sofort wieder aktiv und bieten Dir schnell neue Möglichkeiten an - ohne dass Du erneut Bewerbungen versenden musst! Ein Anruf oder eine Email genügt!</p>
  </div>
  <div class="feat" style="left:104px;top:590px">
    <svg width="40" height="46"><rect x="3" y="3" width="30" height="40" rx="3" fill="none" stroke="#5cb82e" stroke-width="4"/><path d="M10 14h16M10 22h16M10 30h10" stroke="#5cb82e" stroke-width="3"/></svg>
    <h3>Alle Versprechungen findest Du im Arbeitsvertrag</h3>
    <p>In Zusammenarbeit mit Einrichtungen und Kliniken erhalten unsere Kandidaten einen zugesicherten Bonus in Höhe von 750 EUR für das Vertrauen bei Ihrem Jobwechsel in pflegeweg-job.de</p>
  </div>
  <div class="feat" style="left:446px;top:600px">
    <svg width="48" height="36"><ellipse cx="24" cy="18" rx="20" ry="12" fill="none" stroke="#5cb82e" stroke-width="4"/><circle cx="24" cy="18" r="5" fill="#5cb82e"/><path d="M6 34 42 2" stroke="#5cb82e" stroke-width="4"/></svg>
    <h3 style="margin-left:84px">Anonymität</h3>
    <p style="margin-left:84px;width:250px">Wir erstellen ein Profil Deiner Kenntnisse und Fähigkeiten sowie Deiner Berufserfahrung. Weder Dein Name, noch Deine Vorarbeitgeber tauchen im ersten Schritt auf. Erst wenn eine Einrichtung oder Klinik daran Interesse zeigt, entscheiden wir gemeinsam, wie es weitergeht!</p>
  </div>
  <div class="feat" style="left:790px;top:600px">
    <svg width="44" height="40"><circle cx="22" cy="14" r="10" fill="#5cb82e"/><path d="M4 40c2-12 34-12 36 0z" fill="#5cb82e"/></svg>
    <h3 style="margin-left:94px">Keine Zeitarbeit</h3>
    <p style="margin-left:94px;width:220px">Wir vermitteln ausschließlich in Festanstellungen direkt bei Kliniken oder Einrichtungen. Wir können Dir jedoch wertvolle Tipps geben, sollte Zeitarbeit für Dich in Frage kommen ...<b class="green">WIR KENNEN UNS AUS!</b></p>
  </div>
</section>

<section class="about">
  <h2 class="sec-title" style="top:50px;font-size:33px">ÜBER UNS</h2>
  <div class="sec-rule" style="top:100px"></div>
  <p class="sec-sub" style="top:126px">Ihr Erfolg, unser Engagement</p>
  <p>PFLEGEWEG-JOB.de hat es sich mit über 15 Jahren Erfahrung zum Ziel gesetzt, Fachkräften im Gesundheitswesen dabei zu helfen, lohnende Führungspositionen zu finden. Wir sind darauf spezialisiert, qualifizierte Kandidaten mit erstklassigen Gesundheitseinrichtungen zusammenzubringen.</p>
  <span class="btn">Weiter</span>
</section>

<section class="reviews">
  <h2 class="sec-title" style="top:50px;font-size:33px">BEWERBERERFAHRUNG</h2>
  <div class="sec-rule" style="top:100px"></div>
  <p class="sec-sub" style="top:126px;line-height:24px">Bewerber haben Folgendes bei uns erlebt und ihre Erfahrungen<br>geschildert</p>

  <div class="card" style="left:-80px;top:205px;width:410px;height:340px;text-align:left;padding-left:90px">
    <div class="quote" style="margin-left:30px">”</div>
    <p style="margin-top:10px">Lorem Ipsum<br>"Neque Porro Quisquam Est Qui Dolorem Ipsum Quia Dolor Sit Amet, Consectetur, Adipisci Velit..." "There Is No One Who Loves Pain Itself, Who Seeks After It And Wants To Have It, Simply Because It Is Pain..."</p>
    <p style="margin-top:40px;font-size:17px"><b>Moritz Falk</b><br>Mitglied PFLEGEWEG-JOB</p>
  </div>
  <div class="card" style="left:395px;top:260px;width:482px;height:288px">
    <div class="quote">”</div>
    <p>Lorem Ipsum<br>"Neque Porro Quisquam Est Qui Dolorem Ipsum Quia Dolor Sit Amet, Consectetur, Adipisci Velit..." "There Is No One Who Loves Pain Itself, Who Seeks After It And Wants To Have It, Simply Because It Is Pain..."</p>
    <div class="who"><div class="avatar" role="img" aria-label="Porträtfoto des Bewerbers"></div><div><b>Tarek Olsen</b><span>Mitglied PFLEGEWEG-JOB</span></div></div>
  </div>
  <div class="card" style="left:968px;top:205px;width:400px;height:340px">
    <div class="quote" style="text-align:left;margin-left:180px">”</div>
    <p style="margin-top:10px">Lorem Ipsum<br>"Neque Porro Quisquam Est Qui Dolorem Ipsum Quia Dolor Sit Amet, Consectetur..." "There Is No One Who Loves Pain Itself, Who Seeks After It And Wants To Have It..."</p>
    <div class="who"><div class="avatar" role="img" aria-label="Porträtfoto des Bewerbers"></div><div><b>Moritz Falk</b><span>Mitglied PFLEGEWEG</span></div></div>
  </div>
  <div class="arrow" style="left:370px;top:395px"><svg width="14" height="20"><path d="M11 2 3 10l8 8" stroke="#5cb82e" stroke-width="3" fill="none"/></svg></div>
  <div class="arrow" style="left:853px;top:395px"><svg width="14" height="20"><path d="M3 2l8 8-8 8" stroke="#5cb82e" stroke-width="3" fill="none"/></svg></div>
</section>

<section class="contact">
  <h2>Nimm ganz einfach Kontakt zu uns<br>auf:</h2>
  <p class="abs ital" style="left:108px;top:195px;font-size:14px;color:#777">gewünschter Rückruf-Zeitpunkt</p>
  <div class="field" style="left:108px;top:256px;width:264px"><label>Nachname</label><div class="box">Gib deinen Namen ein</div></div>
  <div class="field" style="left:398px;top:256px;width:264px"><label>E-Mail-Adresse</label><div class="box" style="border-color:var(--blue)">John.exp@gml</div></div>
  <div class="field" style="left:108px;top:346px;width:554px"><label>Betreff</label><div class="box" style="height:70px">Geben Sie Ihre Anforderung ein...</div></div>
  <div class="field" style="left:108px;top:456px;width:554px"><label>Nachricht</label><div class="box" style="height:118px">Was möchten Sie vermitteln?</div></div>
  <span class="btn send">Senden</span>

  <div class="panel">
    <h2>KONTAKTDATEN</h2>
    <p class="role">Ansprechpartner</p>
    <div class="portrait" role="img" aria-label="Porträtfoto des Ansprechpartners"></div>
    <p class="name">Herr Jonas Lerch</p>
    <div class="pline"><svg width="18" height="18" viewBox="0 0 24 24"><path fill="#5cb82e" d="M6.6 10.8a15 15 0 0 0 6.6 6.6l2.2-2.2c.3-.3.7-.4 1-.2 1.1.4 2.3.6 3.6.6.6 0 1 .4 1 1V20c0 .6-.4 1-1 1A17 17 0 0 1 3 4c0-.6.4-1 1-1h3.5c.6 0 1 .4 1 1 0 1.3.2 2.5.6 3.6.1.3 0 .7-.2 1z"/></svg>07000 123 456 7</div>
    <div class="pline"><svg width="18" height="14"><rect width="18" height="14" rx="2" fill="#5cb82e"/><path d="M1 1l8 7 8-7" stroke="#fff" stroke-width="2" fill="none"/></svg><u>jonas.lerch@pflegeweg-job.de</u></div>
    <p class="addr">Adresse:</p>
    <div class="pline"><svg width="18" height="22"><path d="M9 21S1 12 1 8a8 8 0 0 1 16 0c0 4-8 13-8 13z" fill="#5cb82e"/><circle cx="9" cy="8" r="3" fill="#fff"/></svg>Werkhof 12, 70100 Musterstadt</div>
    <div class="pline"><svg width="18" height="18" viewBox="0 0 24 24"><path fill="#5cb82e" d="M6.6 10.8a15 15 0 0 0 6.6 6.6l2.2-2.2c.3-.3.7-.4 1-.2 1.1.4 2.3.6 3.6.6.6 0 1 .4 1 1V20c0 .6-.4 1-1 1A17 17 0 0 1 3 4c0-.6.4-1 1-1h3.5c.6 0 1 .4 1 1 0 1.3.2 2.5.6 3.6.1.3 0 .7-.2 1z"/></svg>07000 123 456 7</div>
    <div class="pline"><svg width="18" height="14"><rect width="18" height="14" rx="2" fill="#5cb82e"/><path d="M1 1l8 7 8-7" stroke="#fff" stroke-width="2" fill="none"/></svg><u>info@pflegeweg-job.de</u></div>
    <div class="corner"></div>
  </div>
</section>

<section class="map" role="img" aria-label="Stadtplan mit dem Standort des Büros"></section>

<footer class="footer">
  <div class="brand"><span class="brand-dot" style="width:60px;height:60px"></span>PFLEGEWEG JOB</div>
  <div class="socials"><i></i><i></i><i></i><i></i></div>
  <h4 style="left:422px;top:22px">Seitenverzeichnis</h4>
  <ul><li>HOME</li><li>WIR BIETEN DIR</li><li>ÜBER UNS</li><li>KONTAKT</li></ul>
  <h4 style="left:786px;top:22px">Abonnieren</h4>
  <div class="newsletter"><svg width="18" height="14"><rect x="1" y="1" width="16" height="12" rx="2" fill="none" stroke="#f0a060" stroke-width="2"/></svg>| Geben sie Ihre E-Mail Adresse ein</div>
  <p class="note">Senden Sie eine E-Mail und Sie erhalten regelmäßig unsere Newsletter, Service-Blogs und Pressemitteilungen</p>
</footer>
<p class="copy-strip">Copyright 2024 pflegeweg-job.de, All Right Reserved</p>

</body>
</html>
```